Business Card Design

I need a business card design for a photography business that specializes in headshots and portraits.

Target Market(s)

Business professionals, actors, actresses

Industry/Entity Type

Business

Contact Information for Business Card

Cobalt Ridge Photography, Greg Whitlow, 5817 Kellerman Ave, Suite 416, Fort Wayne, IN 46915, 260.555.0187, www.cobaltridgephoto.example. greg.whitlow@cobaltridgephoto.example

Requirements
Must have
• The business card should state the type of photography services offered: headshots and portraits.

```html
<!DOCTYPE html>
<html lang="en">
<head>
<meta charset="utf-8">
<title>Cobalt Ridge Photography — Business Card</title>
<link rel="stylesheet" href="https://fonts.googleapis.com/css2?family=Montserrat:wght@600;700&family=Roboto+Condensed:wght@300;400&display=swap">
<style>
  :root {
    --backdrop: #b6b6b6;
    --card: #ffffff;
    --brand-blue: #2f5aa8;
    --brand-teal: #2b8c9c;
    --name-blue: #3263b4;
    --text-grey: #6d6d6d;
    --mosaic-deep: #0f4f8a;
    --mosaic-mid: #1467a6;
    --mosaic-light: #1a86c4;
  }
  html, body {
    margin: 0;
    padding: 0;
    width: 1200px;
    height: 900px;
    overflow: hidden;
    background: var(--backdrop);
  }
  .card {
    position: absolute;
    left: 241px;
    top: 204px;
    width: 717px;
    height: 409px;
    background: var(--card);
    overflow: hidden;
  }
  .card__mosaic {
    position: absolute;
    left: 0;
    top: 0;
    width: 248px;
    height: 409px;
  }
  .card__tagline {
    position: absolute;
    left: 314px;
    top: 36px;
    margin: 0;
    font-family: "Montserrat", sans-serif;
    font-weight: 700;
    font-size: 22.5px;
    letter-spacing: -0.4px;
    color: var(--brand-blue);
    white-space: nowrap;
  }
  .card__tagline-accent { color: var(--brand-teal); }
  .card__studio {
    position: absolute;
    left: 317px;
    top: 104px;
    margin: 0;
    font-family: "Roboto Condensed", sans-serif;
    font-weight: 400;
    font-size: 42px;
    line-height: 1;
    color: var(--name-blue);
    white-space: nowrap;
  }
  .card__studio-type {
    position: absolute;
    left: 317px;
    top: 152px;
    margin: 0;
    font-family: "Roboto Condensed", sans-serif;
    font-weight: 400;
    font-size: 19px;
    color: var(--text-grey);
    white-space: nowrap;
  }
  .card__contact {
    position: absolute;
    left: 316px;
    top: 222px;
    margin: 0;
    font-family: "Roboto Condensed", sans-serif;
    font-weight: 400;
    font-size: 18px;
    line-height: 29px;
    color: var(--text-grey);
    font-style: normal;
    white-space: nowrap;
  }
  .card__contact-line { display: block; }
  .card__website {
    position: absolute;
    left: 306px;
    top: 375px;
    margin: 0;
    font-family: "Montserrat", sans-serif;
    font-weight: 600;
    font-size: 17px;
    letter-spacing: -0.3px;
    color: var(--brand-teal);
    white-space: nowrap;
  }
</style>
</head>
<body>
  <div class="card">
    <svg class="card__mosaic" viewBox="0 0 248 409" role="img" aria-label="Geometric mosaic of blue and white triangles">
      <defs>
        <linearGradient id="mosaicTone" x1="0" y1="0" x2="1" y2="1">
          <stop offset="0" stop-color="#0f4f8a"/>
          <stop offset="0.55" stop-color="#1467a6"/>
          <stop offset="1" stop-color="#1a86c4"/>
        </linearGradient>
      </defs>
      <polygon points="0,0 248,0 248,246 124,246 124,328 186,328 124,409 0,409" fill="url(#mosaicTone)"/>
    </svg>

    <h2 class="card__tagline">PHOTOGRAPHY <span class="card__tagline-accent">BUSINESS</span></h2>
    <h1 class="card__studio">Cobalt Ridge</h1>
    <p class="card__studio-type">Headshot &amp; Portrait Photography</p>

    <address class="card__contact">
      <span class="card__contact-line">Greg Whitlow : 5817 Kellerman Ave,</span>
      <span class="card__contact-line">Suite 416, Fort Wayne, IN 46915,</span>
      <span class="card__contact-line">Phone : 260.555.0187</span>
      <span class="card__contact-line">Email : greg.whitlow@cobaltridgephoto.example</span>
    </address>

    <p class="card__website">www.cobaltridgephoto.example</p>
  </div>
</body>
</html>
```